Landing Page Design for Business Page

I need a very attractive landing page designed for my business to obtain customer information. I would like an improvement to an existing landing page we have that is much more appealing and modern.

I have included resources and assets in the below omitted (banner area) Drive folder. I am a big fan of some of the imagery in the "Banners" folder for design.

https://files.plorvex.net/share/7kTqw52LmbHxZpe3Ra9-nVdWUcFs8yJ?mode=view

Here is existing landing page that I would like improved upon.

http://lp4.vurmalpower.net/vmp-lx-signup

```html
<!DOCTYPE html>
<html lang="en">
<head>
<meta charset="utf-8">
<title>Vurmal Power – Free Consultation</title>
<link href="https://fonts.googleapis.com/css2?family=League+Gothic&family=Poppins:wght@400;500;600&family=Roboto:wght@400;500;700&display=swap" rel="stylesheet">
<style>
:root{
  --sky:#19b0e6;
  --grass:#3cc05a;
  --form-green:#4fa83a;
  --orange:#ff7a00;
  --red:#e43a2e;
  --ink:#111;
  --muted:#666;
  --soft-bg:#f7f7f7;
  --bar-track:#e2e2e2;
  --bar-fill:#7cc6e3;
  --teal:#6fd0c4;
  --star:#f4a81d;
  --white:#fff;
}
*{box-sizing:border-box;margin:0;padding:0}
html,body{width:723px;height:1200px;overflow:hidden}
body{position:relative;background:var(--soft-bg);font-family:'Poppins',sans-serif;color:var(--ink)}
.abs{position:absolute}
.display{font-family:'League Gothic',sans-serif;font-weight:400;text-transform:uppercase}

/* hero */
.hero{position:absolute;left:0;top:0;width:723px;height:463px;background:linear-gradient(180deg,var(--sky) 0%,#27b7b3 50%,var(--grass) 100%)}
.brand{left:66px;top:30px;display:flex;align-items:center;gap:8px;color:var(--white);font-size:26px;font-weight:500;letter-spacing:.5px}
.brand-mark{width:22px;height:22px;border:3px solid var(--white)}
.phone{left:502px;top:17px;display:flex;align-items:center;gap:6px;color:var(--white);font-size:23px;letter-spacing:.3px}
.menu{left:640px;top:20px;width:21px}
.menu span{display:block;height:2.5px;background:var(--white);margin-bottom:4.5px}
.hero-title{left:62px;top:129px;width:300px;font-size:31px;line-height:27px;color:var(--white)}
.hero-lead{left:61px;top:200px;width:272px;font-size:12.6px;line-height:19.5px;color:var(--white)}
.hero-offer{left:63px;top:254px;width:292px;font-size:18.6px;line-height:22.4px;color:var(--white)}
.secure{left:63px;top:333px;display:flex;align-items:center;gap:4px;font-size:10.5px;color:var(--white)}
.cta{left:62px;top:365px;width:158px;height:26px;background:var(--red);color:var(--white);font-size:9.5px;font-weight:600;display:flex;align-items:center;justify-content:center;gap:4px}
.pointer{left:276px;top:368px}

/* form */
.consult{left:370px;top:119px;width:291px;height:283px;background:var(--form-green);border-radius:5px}
.consult h2{position:absolute;top:15px;width:100%;text-align:center;font-size:25px;color:var(--white)}
.consult p.sub{position:absolute;top:43px;width:100%;text-align:center;font-size:9.2px;color:var(--white)}
.field{position:absolute;left:12px;width:268px;height:30px;background:var(--white);border-radius:2px;font-size:7px;color:#444;padding-left:10px;display:flex;align-items:center}
.submit{position:absolute;left:12px;top:218px;width:268px;height:30px;background:var(--orange);color:var(--white);font-family:'Roboto',sans-serif;font-weight:500;font-size:9px;display:flex;align-items:center;justify-content:center;border-radius:2px}
.consult p.note{position:absolute;top:255px;width:100%;text-align:center;font-size:7.2px;color:var(--white)}

/* banner */
.promo{left:61px;top:501px;width:602px;height:83px;background:linear-gradient(90deg,#2fb7ea 0%,#5bc07a 40%,#c99a6b 62%,#e9dccb 80%,#ffffff 88%);box-shadow:0 2px 6px rgba(0,0,0,.12)}
.promo-close{left:650px;top:504px;font-size:9px;color:#333}

/* reviews */
.section-title{left:0;top:619px;width:723px;text-align:center;font-size:31px;color:var(--ink)}
.svc-title{left:108px;top:667px;font-family:'Roboto',sans-serif;font-weight:500;font-size:17.5px}
.score{left:108px;top:693px;font-size:22px;font-weight:600}
.score-stars{left:148px;top:697px;color:var(--star);font-size:9px;letter-spacing:-.5px}
.score-count{left:150px;top:711px;font-size:7px;font-weight:500}
.btn{position:absolute;top:735px;width:97px;height:26px;display:flex;align-items:center;justify-content:center;font-family:'Roboto',sans-serif;font-weight:500;font-size:8.5px}
.btn-outline{left:108px;border:1px solid #333;background:var(--white)}
.btn-solid{left:211px;background:var(--orange);color:var(--white)}
.bar-row{position:absolute;left:398px;width:220px;height:12px;display:flex;align-items:center;font-family:'Roboto',sans-serif;font-size:8.5px;color:#555}
.bar-row .lbl{width:42px}
.bar-row .track{width:150px;height:2px;background:var(--bar-track);position:relative}
.bar-row .fill{position:absolute;left:0;top:0;height:2px;background:var(--bar-fill)}
.bar-row .val{margin-left:8px}
.rule{position:absolute;left:66px;width:588px;height:1px;background:#ddd}
.review{position:absolute;top:806px;width:280px}
.review h4{font-family:'Roboto',sans-serif;font-weight:500;font-size:10px;margin-bottom:9px}
.reviewer{display:flex;align-items:center;gap:8px;font-size:8.6px;font-weight:500;height:21px}
.avatar{width:21px;height:21px;border-radius:50%;background:#9a9a9a}
.rating{display:flex;align-items:center;gap:8px;margin-top:5px;font-size:8.6px;font-weight:500}
.rating .stars{color:var(--star);font-size:11px;letter-spacing:-1px}
.where{font-size:8.3px;font-weight:600;margin-top:5px}
.body{font-family:'Roboto',sans-serif;font-size:8.2px;line-height:15.8px;color:var(--muted);margin-top:7px}
.helpful{font-family:'Roboto',sans-serif;font-size:8.4px;font-weight:500;color:var(--teal);margin-top:9px}
.actions{font-family:'Roboto',sans-serif;font-size:8.2px;color:#777;margin-top:7px;word-spacing:2px}
.load-more{left:267px;top:1018px;width:188px;height:30px;background:var(--orange);color:var(--white);font-family:'Roboto',sans-serif;font-weight:500;font-size:9px;display:flex;align-items:center;justify-content:center}

/* footer */
.footer{left:0;top:1098px;width:723px;height:102px;background:#000}
.social{position:absolute;top:25px;width:25px;height:25px;border:1px solid var(--white);border-radius:50%;display:flex;align-items:center;justify-content:center}
.copyright{position:absolute;top:65px;width:100%;text-align:center;color:var(--white);font-size:9.5px}
</style>
</head>
<body>

<section class="hero">
  <div class="abs brand"><span class="brand-mark"></span>Vurmal Power</div>
  <div class="abs phone display">
    <svg width="17" height="17" viewBox="0 0 24 24"><path d="M6.6 10.8a15 15 0 0 0 6.6 6.6l2.2-2.2a1 1 0 0 1 1-.25 11.4 11.4 0 0 0 3.6.57 1 1 0 0 1 1 1V20a1 1 0 0 1-1 1A17 17 0 0 1 3 4a1 1 0 0 1 1-1h3.5a1 1 0 0 1 1 1c0 1.25.2 2.45.57 3.57a1 1 0 0 1-.25 1z" fill="#fff"/></svg>
    555-014-2290
  </div>
  <div class="abs menu"><span></span><span></span><span></span></div>

  <h1 class="abs hero-title display">Claim your free consultation today.</h1>
  <p class="abs hero-lead">Reduce that Utility Bill today.&nbsp; We're offering 10 FREE Consultation this Week.</p>
  <p class="abs hero-offer display">I'm ready to schedule my free consultation and find out if I qualify for 75-100% off insulation &amp; weatherization! No purchase necessary.</p>
  <p class="abs secure">
    <svg width="7" height="9" viewBox="0 0 7 9"><rect x="0" y="4" width="7" height="5" fill="#fff"/><path d="M1.5 4V2.5a2 2 0 0 1 4 0V4" stroke="#fff" fill="none" stroke-width="1.2"/></svg>
    100% Secure. We Never Share Your Email.
  </p>
  <div class="abs cta">
    <svg width="9" height="9" viewBox="0 0 10 10"><circle cx="5" cy="5" r="5" fill="#fff"/><path d="M5 2.3 7.5 5H6v2.6H4V5H2.5z" fill="#e43a2e"/></svg>
    Take Action Today!
  </div>
  <svg class="abs pointer" width="108" height="42" viewBox="0 0 108 42">
    <path d="M3 15 C35 22 70 16 100 5" stroke="#fff" stroke-width="1.6" fill="none"/>
    <path d="M80 3 L104 4 L82 40" stroke="#fff" stroke-width="2" fill="none"/>
  </svg>

  <form class="abs consult">
    <h2 class="display">Free Consultation Form</h2>
    <p class="sub">Fill out your details below to schedule your session!</p>
    <div class="field" style="top:68px">Your Full Name</div>
    <div class="field" style="top:105px">Your Email Address</div>
    <div class="field" style="top:143px">Your Contact Number</div>
    <div class="field" style="top:181px">How soon did you want to complete the weatherization/insulation work?</div>
    <div class="submit">SUBMIT</div>
    <p class="note">We'll Never Misuse Or Share Your Personal Details.</p>
  </form>
</section>

<div class="abs promo" role="img" aria-label="Promotional banner: 75-100% off insulation and weatherization, photo of attic insulation being installed, company name and partner badge with a more information button"></div>
<div class="abs promo-close">✕</div>

<h2 class="abs section-title display">What our customers are saying</h2>
<h3 class="abs svc-title">SERVICE REVIEWS</h3>
<div class="abs score">4.3</div>
<div class="abs score-stars">★★★★★</div>
<div class="abs score-count">883 review</div>
<div class="btn btn-outline">SEE ALL REVIEWS</div>
<div class="btn btn-solid">WRITE A REVIEW</div>

<div class="bar-row" style="top:679px"><span class="lbl">5 Starts</span><span class="track"><span class="fill" style="width:77%"></span></span><span class="val">555</span></div>
<div class="bar-row" style="top:697px"><span class="lbl">4 Starts</span><span class="track"><span class="fill" style="width:61%"></span></span><span class="val">451</span></div>
<div class="bar-row" style="top:715px"><span class="lbl">3 Starts</span><span class="track"><span class="fill" style="width:49%"></span></span><span class="val">150</span></div>
<div class="bar-row" style="top:733px"><span class="lbl">2 Starts</span><span class="track"><span class="fill" style="width:28%"></span></span><span class="val">22</span></div>
<div class="bar-row" style="top:751px"><span class="lbl">1 Starts</span><span class="track"><span class="fill" style="width:11%"></span></span><span class="val">15</span></div>

<div class="rule" style="top:784px"></div>

<article class="review" style="left:66px">
  <h4>Most helpful positive review</h4>
  <div class="reviewer"><span class="avatar" role="img" aria-label="Reviewer portrait"></span>Dana Holt</div>
  <div class="rating"><span class="stars">★★★★★</span>5.0 out of 5 stars It is 100% Original</div>
  <div class="where">Reviewed in New Zealand on 23 October 2020</div>
  <p class="body">Lorem ipsum dolor sit ametectetur adipiscing elit, sed do eiusmod tempor incididunt ut labore et dolore magnaqua. Quis ipsum suspendisse ultrices gravida. Risus commodo viverra maecenas accumsan lacus vel facilisis. Lorem ipsum dolor sit ametectetur adipiscing</p>
  <p class="helpful">441 people found this helpful</p>
  <p class="actions">Helpful &nbsp;| &nbsp;Comment &nbsp;| &nbsp;Report abuse</p>
</article>

<article class="review" style="left:385px">
  <h4>Most helpful positive review</h4>
  <div class="reviewer"><span class="avatar" role="img" aria-label="Reviewer portrait"></span>Dana Holt</div>
  <div class="rating"><span class="stars">★★★★★</span>5.0 out of 5 stars It is 100% Original</div>
  <div class="where">Reviewed in New Zealand on 23 October 2020</div>
  <p class="body">Lorem ipsum dolor sit ametectetur adipiscing elit, sed do eiusmod tempor incididunt ut labore et dolore magnaqua. Quis ipsum suspendisse ultrices gravida. Risus commodo viverra maecenas accumsan lacus vel facilisis. Lorem ipsum dolor sit ametectetur adipiscing</p>
  <p class="helpful">441 people found this helpful</p>
  <p class="actions">Helpful &nbsp;| &nbsp;Comment &nbsp;| &nbsp;Report abuse</p>
</article>

<div class="rule" style="top:1034px"></div>
<div class="abs load-more">LOAD MORE INTERNATIONAL REVIEWS</div>

<footer class="abs footer">
  <span class="social" style="left:300px" aria-label="Website">
    <svg width="11" height="11" viewBox="0 0 12 12" fill="none" stroke="#fff" stroke-width="1"><circle cx="6" cy="6" r="5"/><path d="M1 6h10M6 1c2 2 2 8 0 10M6 1c-2 2-2 8 0 10"/></svg>
  </span>
  <span class="social" style="left:332px" aria-label="Email">
    <svg width="11" height="9" viewBox="0 0 12 9" fill="none" stroke="#fff" stroke-width="1"><rect x=".5" y=".5" width="11" height="8"/><path d="M.5 .5 6 5l5.5-4.5"/></svg>
  </span>
  <span class="social" style="left:365px" aria-label="Chat">
    <svg width="11" height="10" viewBox="0 0 12 11" fill="none" stroke="#fff" stroke-width="1"><path d="M1 1h10v6H5l-3 3V7H1z"/></svg>
  </span>
  <span class="social" style="left:397px" aria-label="Share">
    <svg width="11" height="11" viewBox="0 0 12 12" fill="#fff"><circle cx="9.5" cy="2.5" r="1.8"/><circle cx="2.5" cy="6" r="1.8"/><circle cx="9.5" cy="9.5" r="1.8"/><path d="M2.5 6 9.5 2.5M2.5 6l7 3.5" stroke="#fff" stroke-width="1"/></svg>
  </span>
  <p class="copyright">©Copyright ©2022 Vurmal Power. All Rights Reserved.</p>
</footer>

</body>
</html>
```